3D abstract logo Construction, Kitchen and Bath design and Project Management Business Card Design

I want a 3d abstract logo for a new General Construction, Kitchen and Bath design and Project Management Company located at Philadelphia PA, we want to put our logo in the white color trucks too. I want to look professional and serious at the same time look like an architect design and the warm originals color that make you feel in a nice decorated home, I like the colors trend in this link:
http://www.quillorbit.example/qo/kts/cardmaker.aspx?alt_doc_id=RM41T-K7B93-2W5&doc_id=5130948826&pf_id=H4D

I was thinking about a roof and the PA font could have square shape or like wood framing with two tones of the brick color black and creamy yellow color.... Also I like the keystone Idea like the modification or the LK Skyroute logo but curvy at the top

The final design should communicate big company (because we want to grow), responsible, professional and organized that really care about our customers and give them everything they need... plan and design, excellent labor and Project Management
Updates

I doesn't have to be 3d

Reason: I haven't received enough options...

Please stick with the warm tones shown in the image001 attached I like spicy cinnamon instead a cold wine or brick color and also the cream yellowish tones added

Hello designers, please use only the idea and colors of the image001 I don't want to be stick with a house logo because I do commercial construction too so I prefer work around the keystone idea maybe leaving the style of the PA.
I'd like the base tone on the card dark like first option and you can send me a white option too.

Please send me your ideas as soon as possible 

Thank you so much!

Target Market(s)

Builders, State, commercial business owners, Property owners or Real State and Property Management Companies

Industry/Entity Type

Architect

Contact Information for Business Card

LK Buildworks LLC
“Your project is our business”
Renata Solvik Eng.
President
Commercial & Residential General Construction
Kitchen & Bath Design | Project Management
Phone: 215-738-4196 | Fax: 215-738-4197 Cell: 856-390-7712
renata@lkbuildworks.example

```html
<!DOCTYPE html>
<html lang="en">
<head>
<meta charset="utf-8">
<title>LK Buildworks LLC — Business Card</title>
<link rel="stylesheet" href="https://fonts.googleapis.com/css2?family=Jost:ital,wght@0,400;0,500;0,700;1,400;1,500;1,700;1,800&display=swap">
<style>
  :root {
    --cinnamon: #7b2320;
    --cream-top: #fad3a5;
    --cream-mid: #d3ae84;
    --cream-bottom: #927955;
    --ink: #111111;
    --white: #ffffff;
  }
  * { margin: 0; padding: 0; box-sizing: border-box; }
  html, body {
    width: 1200px; height: 702px; overflow: hidden;
    background: var(--cinnamon);
  }
  .card {
    position: relative;
    width: 1200px; height: 702px;
    background: var(--cinnamon);
    font-family: "Jost", "Century Gothic", sans-serif;
    color: var(--ink);
  }
  .brand-mark {
    position: absolute;
    left: 40px; top: 165px;
    width: 410px;
    display: flex; align-items: center; justify-content: center; gap: 18px;
    color: var(--white);
    font-weight: 700;
    font-size: 46px;
    line-height: 1;
  }
  .brand-mark .square {
    width: 38px; height: 38px;
    background: var(--white);
    flex: none;
  }
  .person {
    position: absolute;
    left: 79px; top: 442px;
  }
  .person-name {
    font-size: 41px; font-weight: 800; font-style: italic;
    line-height: 1.1; letter-spacing: 0.3px;
  }
  .person-title {
    font-size: 26px; font-style: italic; font-weight: 400;
    margin-top: 2px;
  }
  .person-email {
    position: absolute; left: 79px; top: 570px;
    color: var(--white);
    font-size: 23px; font-style: italic; font-weight: 400;
  }
  .person-email b { font-weight: 700; }
  .info-panel {
    position: absolute;
    left: 513px; top: 57px;
    width: 623px; height: 645px;
    background: linear-gradient(180deg, var(--cream-top) 0%, var(--cream-mid) 45%, var(--cream-bottom) 100%);
  }
  .company-name {
    position: absolute; left: 51px; top: 55px;
    font-size: 49px; font-weight: 700; font-style: italic;
    letter-spacing: 0.5px; line-height: 1;
  }
  .tagline {
    position: absolute; left: 51px; top: 113px;
    font-size: 31px; font-weight: 700; font-style: italic;
    line-height: 1;
  }
  .services {
    position: absolute; left: 47px; top: 176px;
    font-size: 22px; font-weight: 400; line-height: 27px;
  }
  .contact {
    position: absolute; left: 57px; top: 411px;
    list-style: none;
    font-size: 23px; font-style: italic; font-weight: 400;
    line-height: 32.5px;
  }
  .contact b { font-weight: 700; }
</style>
</head>
<body>
  <div class="card">
    <div class="brand-mark">
      <span class="square"></span>
      <span class="brand-name">LK Buildworks</span>
    </div>

    <div class="person">
      <div class="person-name">Renata Solvik</div>
      <div class="person-title">President</div>
    </div>
    <div class="person-email"><b>renata@lkbuildworks</b>.example</div>

    <div class="info-panel">
      <h1 class="company-name">LK Buildworks LLC</h1>
      <p class="tagline">“Your project is our business”</p>
      <p class="services">Commercial &amp; Residential General Construction<br>Kitchen &amp; Bath Design &nbsp;| &nbsp;Project Management</p>
      <ul class="contact">
        <li><b>Phone:</b> 215-738-4196</li>
        <li><b>Fax:</b> 215-738-4197</li>
        <li><b>Cell:</b> 856-390-7712</li>
        <li>www.<b>lkbuildworks</b>.example</li>
      </ul>
    </div>
  </div>
</body>
</html>
```